Hydraulics Company Business Card Design

Modern business card design for a hydraulics company.
Our company colours are - black, orange and white.
I would like the following contact details included-
Name
Position
Phone number
Email
Website
Street Address

I have attached our company logo.
I would like the back of the card white.

Thank you.

```html
<!DOCTYPE html>
<html lang="en">
<head>
<meta charset="UTF-8">
<title>Corrin Fluid Power – Business Card</title>
<link rel="stylesheet" href="https://fonts.googleapis.com/css2?family=Montserrat:wght@700&family=Open+Sans:wght@400;600&display=swap">
<style>
  :root {
    --orange: #f7a11a;
    --black: #070707;
    --white: #ffffff;
    --ink: #2a2a2a;
    --stage: #2b2d31;
  }
  * { margin: 0; padding: 0; box-sizing: border-box; }
  html, body { width: 1200px; height: 900px; overflow: hidden; }
  body {
    background: var(--stage);
    display: flex;
    align-items: center;
    justify-content: center;
    gap: 40px;
  }
  .card {
    width: 540px;
    height: 309px;
    position: relative;
    box-shadow: 0 10px 30px rgba(0,0,0,0.45);
  }
  .card--front { background: var(--white); }
  .card--back { background: var(--black); display: flex; align-items: center; justify-content: center; }

  .holder { position: absolute; top: 34px; left: 40px; }
  .holder__name {
    font-family: "Montserrat", sans-serif;
    font-weight: 700;
    font-size: 21px;
    color: var(--orange);
  }
  .holder__role {
    font-family: "Open Sans", sans-serif;
    font-size: 12px;
    color: var(--ink);
    margin-top: 1px;
  }

  .contact {
    position: absolute;
    left: 40px;
    bottom: 34px;
    font-family: "Open Sans", sans-serif;
    font-size: 12.5px;
    color: var(--ink);
    line-height: 1.45;
    list-style: none;
  }
  .contact__address { padding-left: 20px; margin-bottom: 4px; }
  .contact__item { display: flex; align-items: center; gap: 7px; }
  .contact__icon { width: 13px; height: 13px; flex: none; }

  .company-name {
    font-family: "Open Sans", sans-serif;
    font-weight: 600;
    color: var(--orange);
    line-height: 1;
    white-space: nowrap;
  }
  .card--front .company-name { position: absolute; right: 40px; bottom: 92px; font-size: 22px; }
  .card--back .company-name { font-size: 34px; }
</style>
</head>
<body>
  <section class="card card--front" aria-label="Card front">
    <div class="holder">
      <p class="holder__name">Daniel Marlow</p>
      <p class="holder__role">Managing Director</p>
    </div>

    <ul class="contact">
      <li class="contact__address">48 Quarry Road,<br>Riverton, USA</li>
      <li class="contact__item">
        <svg class="contact__icon" viewBox="0 0 16 16" aria-hidden="true"><path fill="#f7a11a" d="M3.5 1.5l2.5 2.8-1.4 2a8 8 0 0 0 5.1 5.1l2-1.4 2.8 2.5-1.6 2.2C7 14.3 1.7 9 1.3 3.1z"/></svg>
        <span>(08) 5550 0142</span>
      </li>
      <li class="contact__item">
        <svg class="contact__icon" viewBox="0 0 16 16" aria-hidden="true"><rect x="1" y="3" width="14" height="10" fill="#f7a11a"/><path d="M1.5 3.5L8 9l6.5-5.5" fill="none" stroke="#fff" stroke-width="1.3"/></svg>
        <span>info@corrinfluid.com</span>
      </li>
      <li class="contact__item">
        <svg class="contact__icon" viewBox="0 0 16 16" aria-hidden="true"><circle cx="8" cy="8" r="7" fill="#f7a11a"/><path d="M1 8h14M8 1c-3 3.5-3 10.5 0 14M8 1c3 3.5 3 10.5 0 14" fill="none" stroke="#fff" stroke-width="1"/></svg>
        <span>www.corrinfluid.com</span>
      </li>
    </ul>

    <p class="company-name">Corrin Fluid Power</p>
  </section>

  <section class="card card--back" aria-label="Card back">
    <p class="company-name">Corrin Fluid Power</p>
  </section>
</body>
</html>
```